Guaranteed Job - Sleek Sexy Business Card UV Spot

Im looking for a sleek and sexy business card, that resembles elite or VIP status status.
our business is corinvale.example
you can view our products on there, but our main audience for handing out our cards will be for people in the hospitality industry, so it will need to impress high management and CEO of hotels and restaurants, bars, clubs etc...
the card features will have UV spot on both sides, 400gsm stock. standard size.
Artwork should be 86 x 54mm + 2mm bleed = 90 x 58mm
it should have a nice "unique" uv spot pattern that highlights the card, not a repeated pattern, theres no originality there, and it will be disregarded.
The written material will be:
Corin Vale Hospitality College (logo)
Tobin Marsh
Director
Phone: 1300 615 737
Mobile: 0455 817 296
Email: info@corinvale.example
website: www.corinvale.example
I'm looking for originality here, i don't want just a simple stock card, want something that has a wow factor for people.
You will find the logo attached. you may invert the white to black words to suit the background as you please.
thank you and good luck
As a side note, ive received a lot of proposals, im too busy to give feedback to each and every one, so if i havent provided feedback for your design within 24 hours, then consider it not acceptable, and you could resubmit another design.
So far i have not seen any design that stood out for me, they all seem pretty generic. there nothing thats unique, i would figure for the amount that im offering, that people would put some more effort and creativity into the design.
so far over 200 designs submitted, and nothing i have seen looks very original, everything looks like a different variation of the same stuff, i said it very clearly i wanted something unique, the only thing that has come close to it so far is this one
Reason: Ive received alot of design concepts and i have reviewed everyone, but i havent had time to give feedback to every single one, only the ones that have interested me, if i havent responded, its because i havent found it good enough.
so far only a few design have been on par with what ive been looking for, an attractive eye popping design.
heres a few of them,
http://files.pixelbazaar.example/design_img/51736/62418/62418_2840915_51736_image.jpg
http://files.pixelbazaar.example/design_img/51736/68254/68254_2841377_51736_image.jpg
theyre, both unique and original, and eye catching, the only thing theyre missing is the sexyness.
if you still think you have some creativity left in your minds, then throw it on here.
Reason: Sorry guys for the delay, I was in a serious accident and out of commission for the past few months, I'm just slowly recovering now, please bare with me as i try to attend to this project, it may take me awhile as I have other projects that are on standby, I'm not 100% at the moment, so im extending the deadline for 2 weeks right now. Thanks for your patience.
Hospitality

```html
<!DOCTYPE html>
<html lang="en">
<head>
<meta charset="utf-8">
<title>Corin Vale Hospitality College – Business Card</title>
<link rel="stylesheet" href="https://fonts.googleapis.com/css2?family=Bebas+Neue&family=Oswald:wght@500&family=Quicksand:wght@500;700&display=swap">
<style>
  :root{
    --canvas:#272727;
    --card-top:#333333;
    --card-bottom:#1b1b1b;
    --card-edge:#555555;
    --accent:#4ea3f0;
    --accent-deep:#1f5fc9;
    --accent-pale:#6cb8f7;
    --hex-tone:#55a6d6;
    --text-light:#f2f2f2;
    --text-grey:#a9a9a9;
    --ghost:#454545;
  }
  *{margin:0;padding:0;box-sizing:border-box}
  html,body{width:1200px;height:900px;overflow:hidden;background:var(--canvas)}
  body{position:relative;font-family:"Quicksand",sans-serif}

  .side-label{
    position:absolute;left:368px;
    font-family:"Bebas Neue",sans-serif;font-size:46px;line-height:1;
    color:var(--accent);letter-spacing:0.5px;
  }
  .side-label--front{top:86px}
  .side-label--back{top:435px}

  .card{
    position:absolute;left:369px;width:452px;height:273px;
    background:linear-gradient(180deg,var(--card-top) 0%,#2a2a2a 45%,var(--card-bottom) 100%);
    border:1px solid var(--card-edge);
    overflow:hidden;
    box-shadow:0 2px 6px rgba(0,0,0,.35);
  }
  .card--front{top:131px}
  .card--back{top:480px}

  .front-band{
    position:absolute;left:0;top:0;width:100%;height:14px;
    background:linear-gradient(90deg,var(--accent-pale) 0%,var(--accent) 45%,var(--accent-deep) 100%);
  }

  .brand{position:absolute;text-align:right;line-height:1}
  .brand__name{
    display:flex;align-items:center;justify-content:flex-end;gap:5px;
    font-family:"Oswald",sans-serif;font-weight:500;font-size:17px;
    color:var(--text-light);letter-spacing:0.6px;text-transform:uppercase;
  }
  .brand__mark{width:9px;height:9px;background:var(--accent);display:inline-block}
  .brand__sub{
    font-family:"Quicksand",sans-serif;font-weight:500;font-size:7.5px;
    color:var(--text-light);letter-spacing:0.4px;text-transform:uppercase;margin-top:1px;
  }
  .brand--front{right:19px;top:42px}
  .brand--back{right:80px;top:172px}

  .contact{
    position:absolute;right:19px;top:96px;text-align:right;
    text-transform:uppercase;font-size:12px;line-height:15.4px;
  }
  .contact__name{font-weight:700;color:var(--accent)}
  .contact__role{font-weight:700;color:var(--text-grey)}
  .contact__line{font-weight:500;color:var(--text-light)}
  .contact__label{color:var(--accent)}

  .ghost-brand{
    position:absolute;left:-2px;top:170px;
    font-family:"Oswald",sans-serif;font-weight:500;color:var(--ghost);
    text-transform:uppercase;line-height:0.95;
    display:flex;align-items:flex-end;gap:22px;
  }
  .ghost-brand__mark{width:100px;height:100px;background:var(--ghost);opacity:.55}
  .ghost-brand__words{font-size:42px;letter-spacing:1px;padding-bottom:2px}
  .ghost-brand__words small{display:block;font-size:15px;letter-spacing:1.2px;margin-top:2px}

  .uv-pattern{
    position:absolute;left:0;top:0;width:180px;height:162px;
    background:radial-gradient(ellipse at 30% 25%,rgba(85,166,214,.95) 0%,rgba(85,166,214,.75) 45%,rgba(85,166,214,0) 75%);
  }

  .back-rule{
    position:absolute;left:50px;top:205px;width:378px;height:2px;
    background:linear-gradient(90deg,rgba(78,163,240,0) 0%,var(--accent) 35%,var(--accent) 100%);
  }
  .back-band{
    position:absolute;right:0;top:0;width:23px;height:100%;
    background:linear-gradient(180deg,var(--accent-deep) 0%,#3a8ef0 40%,var(--accent-pale) 100%);
  }
</style>
</head>
<body>

  <h2 class="side-label side-label--front">Front</h2>
  <section class="card card--front">
    <div class="front-band"></div>

    <div class="ghost-brand" aria-hidden="true">
      <span class="ghost-brand__mark"></span>
      <span class="ghost-brand__words">Corin<br>Vale<small>Hospitality College</small></span>
    </div>

    <div class="brand brand--front">
      <div class="brand__name"><span class="brand__mark"></span>Corin Vale</div>
      <div class="brand__sub">Hospitality College</div>
    </div>

    <div class="contact">
      <div class="contact__name">Tobin Marsh</div>
      <div class="contact__role">Director</div>
      <div class="contact__line"><span class="contact__label">Phone:</span> 1300 615 737</div>
      <div class="contact__line"><span class="contact__label">Mobile:</span> 0455 817 296</div>
      <div class="contact__line"><span class="contact__label">Email:</span> info@corinvale.example</div>
      <div class="contact__line"><span class="contact__label">Website:</span> www.corinvale.example</div>
    </div>
  </section>

  <h2 class="side-label side-label--back">Back</h2>
  <section class="card card--back">
    <div class="uv-pattern" role="img" aria-label="Cluster of blue UV spot hexagons of varying sizes"></div>

    <div class="brand brand--back">
      <div class="brand__name"><span class="brand__mark"></span>Corin Vale</div>
      <div class="brand__sub">Hospitality College</div>
    </div>

    <div class="back-rule"></div>
    <div class="back-band"></div>
  </section>

</body>
</html>
```